Business Card Design

I need a business card for my corporation. We are a fast food Mexican Taqueria located in San Jose, CA. I want the cards to include our business logo. The cards need to be simple but elegant. Our theme through out our locations is a beach feel atmosphere. I would like to see cards with a beach feeling. Our website is tacoslapalmera.net and it would be great if the cards matched our website.

Industry/Entity Type

Business

Contact Information for Business Card

Marisol Fuentes, VP
2417 Cedar Brook Ave
San Jose, CA 95482
Direct: 4087326159

```html
<!DOCTYPE html>
<html lang="en">
<head>
<meta charset="utf-8">
<title>La Palmera – Business Card</title>
<link href="https://fonts.googleapis.com/css2?family=Open+Sans:wght@300;400;700&display=swap" rel="stylesheet">
<style>
  :root {
    --backdrop: #e9e6e1;
    --card: #f2f2f3;
    --red: #b51f28;
    --grey: #a0a0a0;
    --ink: #111111;
    --text: #2a2a2a;
  }
  * { margin: 0; padding: 0; box-sizing: border-box; }
  html, body { width: 1200px; height: 1111px; overflow: hidden; }
  body {
    background: var(--backdrop);
    font-family: "Open Sans", Arial, sans-serif;
    position: relative;
  }
  .card {
    position: absolute;
    left: 220px;
    width: 760px;
    height: 440px;
    background: var(--card);
    overflow: hidden;
    box-shadow: 0 4px 14px rgba(0,0,0,0.18);
  }
  .card--back { top: 90px; }
  .card--front { top: 581px; }

  .block { position: absolute; border-radius: 0 0 4px 4px; }
  .block--red { background: var(--red); top: 0; }
  .block--grey { background: var(--grey); bottom: 0; border-radius: 4px 4px 0 0; }

  .tick { position: absolute; height: 11px; background: var(--red); border-radius: 3px; }
  .rule { position: absolute; height: 11px; background: var(--grey); border-radius: 3px; }

  .brand {
    position: absolute;
    text-align: center;
    color: var(--red);
    font-weight: 400;
    font-size: 34px;
    line-height: 1;
  }

  /* back face */
  .card--back .block--red { left: 296px; width: 168px; height: 172px; }
  .card--back .block--grey { left: 296px; width: 168px; height: 168px; }
  .card--back .brand { left: 230px; width: 300px; top: 196px; }
  .card--back .tick--left { left: -4px; top: 290px; width: 70px; }
  .card--back .tick--right { right: -4px; top: 176px; width: 70px; }

  /* front face */
  .card--front .block--red { left: 106px; width: 171px; height: 176px; }
  .card--front .block--grey { left: 106px; width: 171px; height: 178px; }
  .card--front .brand { left: 42px; width: 300px; top: 200px; }
  .card--front .tick--left { left: -4px; top: 217px; width: 70px; }
  .card--front .rule { left: 321px; top: 217px; width: 333px; }
  .card--front .tick--right { right: -4px; top: 217px; width: 70px; }

  .details {
    position: absolute;
    right: 106px;
    text-align: right;
  }
  .city {
    top: 118px;
    font-weight: 700;
    font-size: 38px;
    color: var(--ink);
    letter-spacing: 0.5px;
    line-height: 1;
  }
  .city__accent { color: var(--red); }
  .district {
    top: 166px;
    font-weight: 300;
    font-size: 22px;
    color: var(--text);
    line-height: 1;
  }
  .person {
    top: 250px;
    font-weight: 300;
    font-size: 24px;
    color: var(--red);
    line-height: 1;
  }
  .contact {
    top: 300px;
    font-weight: 400;
    font-size: 16.5px;
    color: var(--ink);
    line-height: 27px;
  }
</style>
</head>
<body>

  <section class="card card--back" aria-label="Card back">
    <div class="block block--red"></div>
    <p class="brand">La Palmera</p>
    <div class="block block--grey"></div>
    <div class="tick tick--left"></div>
    <div class="tick tick--right"></div>
  </section>

  <section class="card card--front" aria-label="Card front">
    <div class="block block--red"></div>
    <p class="brand">La Palmera</p>
    <div class="block block--grey"></div>
    <div class="tick tick--left"></div>
    <div class="rule"></div>
    <div class="tick tick--right"></div>

    <h1 class="details city">SAN <span class="city__accent">JOSE</span></h1>
    <p class="details district">CEDAR BROOK</p>
    <p class="details person">MARISOL FUENTES</p>
    <p class="details contact">
      VP 2417 Cedar Brook Ave San Jose<br>
      CA 95482<br>
      Direct: 4087326159
    </p>
  </section>

</body>
</html>
```